Business Card

We are looking to re-create our business card. Attached is the company logo. we would like it to be back and front. for example one side with the persons information and the other side with the company logo. Be as creative as you would like but also keep in mind, we are a Health Insurance company and we need to look professional as well.
Industry/Entity Type
Business

```html
<!DOCTYPE html>
<html lang="en">
<head>
<meta charset="utf-8">
<title>Wellpath Cover Group – Business Card</title>
<link rel="stylesheet" href="https://fonts.googleapis.com/css2?family=Open+Sans:wght@400;600;700&family=Quicksand:wght@300;400&display=swap">
<style>
  :root {
    --backdrop: #a9aaa9;
    --card-white: #ffffff;
    --ink-grey: #8c8c8c;
    --rule-grey: #c9c9c9;
    --brand-blue: #1a8ccc;
    --blue-light: #4db0de;
    --blue-deep: #1583c3;
    --on-blue: #ffffff;
  }
  * { margin: 0; padding: 0; box-sizing: border-box; }
  html, body {
    width: 1200px;
    height: 918px;
    overflow: hidden;
    background: var(--backdrop);
  }
  .canvas {
    position: relative;
    width: 1200px;
    height: 918px;
  }
  .card {
    position: absolute;
    left: 280px;
    width: 640px;
    height: 360px;
    box-shadow: 0 6px 18px rgba(0, 0, 0, 0.18);
  }

  /* Contact side */
  .card--contact {
    top: 60px;
    background: var(--card-white);
  }
  .divider {
    position: absolute;
    left: 250px;
    top: 40px;
    width: 1px;
    height: 250px;
    background: var(--rule-grey);
  }
  .person-name {
    position: absolute;
    right: 404px;
    top: 96px;
    font-family: "Quicksand", sans-serif;
    font-weight: 300;
    font-size: 34px;
    color: var(--ink-grey);
    white-space: nowrap;
  }
  .contact-labels,
  .contact-values {
    position: absolute;
    top: 168px;
    font-family: "Open Sans", sans-serif;
    font-size: 14px;
    line-height: 22px;
  }
  .contact-labels {
    right: 404px;
    text-align: right;
    color: var(--ink-grey);
    font-style: italic;
  }
  .contact-values {
    left: 264px;
    color: var(--brand-blue);
  }
  .wordmark {
    position: absolute;
    display: flex;
    align-items: center;
    gap: 6px;
    font-family: "Open Sans", sans-serif;
    font-weight: 700;
    letter-spacing: -1px;
  }
  .wordmark__square {
    display: block;
    width: 12px;
    height: 12px;
  }
  .card--contact .wordmark {
    right: 404px;
    top: 232px;
    font-size: 28px;
    color: var(--ink-grey);
  }
  .card--contact .wordmark__square { background: var(--brand-blue); }
  .company-name {
    position: absolute;
    left: 264px;
    top: 262px;
    font-family: "Open Sans", sans-serif;
    font-weight: 600;
    font-size: 24px;
    color: var(--brand-blue);
    white-space: nowrap;
  }

  /* Brand side */
  .card--brand {
    top: 498px;
    background: radial-gradient(ellipse at 55% 50%, var(--blue-light) 0%, var(--blue-deep) 75%);
  }
  .brand-lockup {
    position: absolute;
    left: 0;
    right: 0;
    top: 0;
    bottom: 0;
    display: flex;
    align-items: center;
    justify-content: center;
    gap: 22px;
  }
  .card--brand .wordmark {
    position: static;
    font-size: 40px;
    color: var(--on-blue);
  }
  .card--brand .wordmark__square { background: var(--on-blue); width: 14px; height: 14px; }
  .brand-rule {
    width: 2px;
    height: 76px;
    background: var(--on-blue);
  }
  .brand-name {
    font-family: "Open Sans", sans-serif;
    font-weight: 400;
    font-size: 30px;
    color: var(--on-blue);
    white-space: nowrap;
  }
</style>
</head>
<body>
<main class="canvas">
  <section class="card card--contact" aria-label="Card back with contact details">
    <div class="divider"></div>
    <h1 class="person-name">Name Here</h1>
    <div class="contact-labels">
      <p>phone:</p>
      <p>email:</p>
    </div>
    <div class="contact-values">
      <p>+61 (0) 400 555 019</p>
      <p>hello@wellpathcover.com</p>
    </div>
    <div class="wordmark"><span>WCG</span><span class="wordmark__square"></span></div>
    <p class="company-name">Wellpath Cover Group</p>
  </section>

  <section class="card card--brand" aria-label="Card front with company name">
    <div class="brand-lockup">
      <div class="wordmark"><span>WCG</span><span class="wordmark__square"></span></div>
      <div class="brand-rule"></div>
      <p class="brand-name">Wellpath Cover Group</p>
    </div>
  </section>
</main>
</body>
</html>
```